Summer Sale Graphics for Social Media

I want to create 11 social media graphics (new Instagram size 4:5 (1080 x 1350 pixels) focusing on our Summer Sale Graphics, using any of the pics attached. Use the attached pics, NO RANDOM STOCK PHOTOGRAPHY. For the color scheme of the graphics, they should all be complementary to the product colors in the photos.
You can add any of the photos attached but none are required. You can do some of the graphics in all text. I mainly need BOLD text that says one of the headlines (11 total) SEE ATTACHED WORD DOCUMENT for the headlines to use.

```html
<!DOCTYPE html>
<html lang="en">
<head>
<meta charset="utf-8">
<title>Summer Sale Social Graphics</title>
<link href="https://fonts.googleapis.com/css2?family=Audiowide&family=Roboto+Condensed:wght@700&family=Tinos&display=swap" rel="stylesheet">
<style>
  :root {
    --stage: #5a3420;
    --coral: #e8694f;
    --ink-circle: rgba(40, 36, 40, 0.88);
    --photo-warm-a: #8a6a55;
    --photo-warm-b: #3e4a2c;
    --photo-kitchen-a: #7a5646;
    --photo-kitchen-b: #e9e6e2;
    --photo-product-a: #f2f1ef;
    --photo-product-b: #d9d6d3;
    --cream: #f3f1ec;
    --periwinkle: #5f7be6;
    --violet-bar: #6a5fcc;
    --rose: #d97a8a;
    --plum: #a65a90;
    --plum-deep: #6b2d5a;
    --white: #ffffff;
  }
  * { margin: 0; padding: 0; box-sizing: border-box; }
  html, body { width: 1086px; height: 1200px; overflow: hidden; }
  body { background: var(--stage); position: relative; }

  .post { position: absolute; width: 483px; height: 483px; overflow: hidden; }
  .post--circle { left: 53px; top: 71px; }
  .post--detox { left: 561px; top: 71px; background: var(--periwinkle); }
  .post--snatched { left: 53px; top: 583px; background: var(--rose); }
  .post--waist { left: 561px; top: 583px; background: var(--plum); }

  .photo { position: absolute; }
  .photo--full { left: 0; top: 0; width: 100%; height: 100%; }
  .photo--lounge { background: linear-gradient(120deg, var(--photo-warm-a), #6b4a3a 45%, var(--photo-warm-b)); }
  .photo--kitchen { background: linear-gradient(180deg, var(--photo-kitchen-a) 0%, #6b4a3e 60%, var(--photo-kitchen-b) 100%); }
  .photo--products { background: linear-gradient(180deg, var(--photo-product-a), var(--photo-product-b)); }

  .abs { position: absolute; }
  .display { font-family: "Audiowide", sans-serif; }
  .condensed { font-family: "Roboto Condensed", sans-serif; font-weight: 700; }
  .serif { font-family: "Tinos", serif; }

  /* post 1 */
  .promo-circle { left: 257px; top: 278px; width: 202px; height: 202px; border-radius: 50%; background: var(--ink-circle); }
  .promo-circle__title { left: 225px; width: 266px; text-align: center; color: var(--coral); }
  .promo-circle__offer { left: 257px; width: 202px; top: 447px; text-align: center; color: var(--white); font-size: 11px; }

  /* post 2 */
  .detox-strip { left: 0; top: 0; width: 92px; height: 483px; background: var(--cream); }
  .detox-headline { right: 11px; top: 96px; text-align: right; color: var(--white); font-size: 40px; line-height: 45.5px; text-transform: uppercase; }
  .sale-bar { display: flex; align-items: center; justify-content: flex-end; color: var(--white); }
  .detox-sale { left: 245px; top: 345px; width: 238px; height: 55px; background: var(--violet-bar); padding-right: 19px; font-size: 27px; color: #eceaf6; }
  .offer-note { color: var(--white); font-size: 11px; text-align: right; }
  .rule { height: 1px; background: rgba(255,255,255,0.75); }

  /* post 3 */
  .snatched-headline { right: 11px; top: 136px; text-align: right; color: var(--white); font-size: 28px; line-height: 38px; }
  .snatched-sub { right: 11px; top: 259px; text-align: right; color: var(--white); font-size: 38px; line-height: 45px; }

  /* post 4 */
  .waist-headline { left: 39px; top: 35px; color: var(--white); font-size: 28px; line-height: 38px; }
  .waist-band { left: 0; top: 279px; width: 483px; height: 204px; background: var(--white); }
  .waist-foot { left: 37px; top: 417px; width: 446px; height: 66px; background: var(--plum); }
  .waist-sale { left: 257px; top: 336px; width: 226px; height: 55px; background: var(--plum-deep); padding-right: 37px; font-size: 21px; }
</style>
</head>
<body>

<section class="post post--circle">
  <div class="photo photo--full photo--lounge" role="img" aria-label="Smiling woman in a brown top holding three supplement bottles in a lounge"></div>
  <div class="abs promo-circle"></div>
  <p class="abs display promo-circle__title" style="top:322px;font-size:17px;">Summer’s Here</p>
  <p class="abs display promo-circle__title" style="top:350px;font-size:17px;line-height:24px;">And We’re Having<br>the Biggest Sale of<br>the Year</p>
  <p class="abs condensed promo-circle__offer">Up to $15 OFF</p>
</section>

<section class="post post--detox">
  <div class="abs detox-strip"></div>
  <div class="photo photo--kitchen" style="left:23px;top:51px;width:234px;height:390px;" role="img" aria-label="Woman in a white cropped sweater holding a supplement bottle in a kitchen"></div>
  <h2 class="abs condensed detox-headline">Detox,<br>Burn Fat,<br>and Turn<br>Heads This<br>Summer</h2>
  <div class="abs condensed sale-bar detox-sale">SALE NOW!</div>
  <p class="abs serif offer-note" style="right:27px;top:438px;">Up to $15 OFF</p>
  <div class="abs rule" style="left:273px;top:460px;width:190px;"></div>
</section>

<section class="post post--snatched">
  <div class="photo photo--kitchen" style="left:0;top:0;width:253px;height:483px;" role="img" aria-label="Woman in a white sweater behind a row of supplement bottles and creams"></div>
  <h2 class="abs display snatched-headline">GET<br>SNATCHED<br>FOR SUMMER</h2>
  <p class="abs condensed snatched-sub">Supplements<br>On Sale Now!</p>
  <p class="abs serif offer-note" style="right:11px;top:441px;">Up to $15 OFF</p>
</section>

<section class="post post--waist">
  <div class="abs waist-band"></div>
  <div class="abs waist-foot"></div>
  <h2 class="abs display waist-headline">Slim Waist.<br>Flat Tummy.<br>More Energy.<br>Let’s Go!</h2>
  <div class="photo photo--products" style="left:35px;top:212px;width:191px;height:244px;" role="img" aria-label="White supplement bottles on a light studio surface"></div>
  <div class="photo photo--lounge" style="left:257px;top:35px;width:226px;height:301px;" role="img" aria-label="Smiling woman in a brown top holding supplement bottles beside a pool table"></div>
  <div class="abs display sale-bar waist-sale">SALE NOW!</div>
  <p class="abs serif offer-note" style="right:38px;top:434px;">Upto $15 OFF</p>
  <div class="abs rule" style="left:254px;top:456px;width:190px;"></div>
</section>

</body>
</html>
```